Business Card Design Project

I am community manager and social media strategist. I need a double sided business card with company logo and name. Looking for something professional, elegant but also a little bit original.

• - The logo and the colours are the company colours and a required to stay.
- The size should be: 84 x 55 mm (or 3.30 x 2.16)
- The file size should be: 1039 x 697 pixels (300 dpi)
- I'd like rounded corners. :)

Use the following contact information for the card:

Léonie Vardin
Stratégie médias sociaux / community management / édition de sites sociaux
mob. : 0687529103
leonie.vardin@postelune.fr
Twitter. : @lvardin
Skype : vardin.leonie

```html
<!DOCTYPE html>
<html lang="fr">
<head>
<meta charset="utf-8">
<title>Norvelle – cartes de visite</title>
<link href="https://fonts.googleapis.com/css2?family=Arimo:wght@400;700&display=swap" rel="stylesheet">
<style>
  :root{
    --stage-light:#8c8c8c;
    --stage-dark:#5e5e5e;
    --blue-deep:#0e6fae;
    --blue-bright:#22a3de;
    --blue-ink:#0f5d98;
    --blue-soft:#2f9ad6;
    --pale-ring:#e6f0f7;
    --white:#ffffff;
  }
  *{box-sizing:border-box;margin:0;padding:0}
  html,body{width:1200px;height:900px;overflow:hidden}
  body{
    font-family:"Arimo",Arial,sans-serif;
    background:radial-gradient(ellipse at 50% 45%,var(--stage-light),var(--stage-dark) 85%);
    position:relative;
  }
  .card{position:absolute;left:336px;width:562px;border-radius:22px}
  .tab{position:absolute;width:22px;height:272px;border-radius:8px}
  .tab--left{left:-10px}
  .tab--right{right:-10px}

  /* front */
  .card--front{
    top:44px;height:376px;
    background:radial-gradient(ellipse at 50% 100%,var(--blue-bright),var(--blue-deep) 75%);
  }
  .card--front .tab{background:var(--white);top:68px}
  .brand-front{
    position:absolute;left:0;right:0;top:100px;
    display:flex;flex-direction:column;align-items:center;gap:22px;
  }
  .brand-dot{width:120px;height:120px;border-radius:50%;background:var(--white)}
  .brand-name{font-weight:700;font-size:56px;letter-spacing:2px;color:var(--white);line-height:1}

  /* back */
  .card--back{top:468px;height:376px;background:var(--white)}
  .card--back .tab{background:linear-gradient(var(--blue-bright),var(--blue-deep));top:66px}
  .back-clip{position:absolute;inset:0;border-radius:22px;overflow:hidden}
  .faint-ring{
    position:absolute;left:294px;top:132px;width:280px;height:280px;border-radius:50%;
    border:28px solid var(--pale-ring);
  }
  .brand-back{
    position:absolute;left:30px;top:102px;width:200px;
    display:flex;flex-direction:column;align-items:center;gap:10px;
  }
  .brand-back .brand-dot{width:108px;height:108px;background:var(--blue-ink)}
  .brand-back .brand-name{font-size:34px;letter-spacing:1px;color:var(--blue-ink)}
  .divider{position:absolute;left:246px;top:106px;width:2px;height:160px;background:var(--blue-soft)}
  .contact{position:absolute;left:262px;top:104px;color:var(--blue-soft)}
  .person{font-size:40px;line-height:1;color:var(--blue-ink)}
  .person span{color:var(--blue-soft)}
  .line{font-size:17px;margin-top:18px;line-height:1}
  .line + .line{margin-top:12px}
  .socials{display:flex;gap:48px;margin-top:22px;font-size:15px;line-height:1}
  .social{display:flex;align-items:center;gap:8px}
  .social-square{width:16px;height:16px;border-radius:3px;background:var(--blue-soft)}
  .tagline{position:absolute;left:0;right:0;top:286px;text-align:center;font-size:14px;color:var(--blue-soft)}
</style>
</head>
<body>
  <section class="card card--front" aria-label="Recto">
    <div class="tab tab--left"></div>
    <div class="tab tab--right"></div>
    <div class="brand-front">
      <div class="brand-dot"></div>
      <div class="brand-name">NORVELLE</div>
    </div>
  </section>

  <section class="card card--back" aria-label="Verso">
    <div class="tab tab--left"></div>
    <div class="tab tab--right"></div>
    <div class="back-clip">
      <div class="faint-ring"></div>
      <div class="brand-back">
        <div class="brand-dot"></div>
        <div class="brand-name">NORVELLE</div>
      </div>
      <div class="divider"></div>
      <div class="contact">
        <p class="person">Léonie <span>Vardin</span></p>
        <p class="line">mob: 0687529103</p>
        <p class="line">email: leonie.vardin@postelune.fr</p>
        <div class="socials">
          <span class="social"><span class="social-square"></span>@lvardin</span>
          <span class="social"><span class="social-square"></span>vardin.leonie</span>
        </div>
      </div>
      <p class="tagline">Stratégie médias sociaux / community management / édition de sites sociaux</p>
    </div>
  </section>
</body>
</html>
```